FenderPals Personal Injury Lawyers Website (Wordpress)

We need a brand new website for our firm's new rebranding. The name of the website is www.fenderpals-example.com. Our new brand will be a group of personal injury lawyers focused on representing only victims in car wrecks. We will be distinguishing ourselves from other law firms due to the fact that other law firms represent clients involving all forms of personal injury. We will only focus on car wrecks and this needs to be reflected on the website.

I have attached the new firm logo and stationary to show the designers the kind of look we are going for in the new website. It needs to be clean, pure, and show the potential clients that we only do one thing and we do it well. That thing is car wrecks.

Some examples of websites that we like are the following:
www.qvt-example.lu - nice interface and colors. nice navigation, we really like the biography pages for the individuals attorneys
www.morvantlegal-example.com - good layout, good navigation
www.pelliardwoss-example.com - navigation bar follows the user whether the user goes up or down

We would like five separate pages -- (1) Home, (2) Client Resources, (3) Expertise / Car Wrecks, (4) Contact Us, (5) News

The Home page will be used for driving traffic and should have a call to action on the right at the top stating that we will send an ebook to anyone who gives their contact information. The ebook will explain how car wrecks work. This should also have room for youtube videos which will be added later.

The client resources will include blogs, books, and information for potential clients. It should be presented in a well developed manner which is both appealing to potential and current clients.

The expertise page will show that we only focus on car wrecks. This needs to be a recurrent theme throughout the entire website. This page will focus on car wrecks and the different aspects including damages, insurance, and investigation.

The Contact Us page will show a google map to our address and phone number. Please use generic information and we will fill in the gaps upon the selection.

News: the news page will show different articles related to past and present cases and the successes of those clients.

The overall page should be elegant and creative. Do not include courthouses, gavels or anything else related to the law. If you include these things, your design will automatically be excluded.
Updates

Please take note this design is now guaranteed. I look forward to receiving everyone's wonderful designs.

Target Market(s)

Persons involved in car wrecks

Industry/Entity Type

Legal

Coding

Coded - Design and coding required

Number of Pages Required

5+ page

Font styles to use
Serif
Sans Serif

Colors
ec1f27
ffffff
000000

Requirements
Must have
• Five pages which focus on representation of car wreck victims. The site must be clean and easy to navigate.
Nice to have
• Navigation bar should follow user up and down the page.
Should not have
• Gavels, court houses, anything related to the law. If your design has these aspects, it will automatically be rejected

```html
<!DOCTYPE html>
<html lang="en">
<head>
<meta charset="utf-8">
<title>FenderPals – Personal Injury Lawyers</title>
<link href="https://fonts.googleapis.com/css2?family=Noto+Serif:wght@400;700&family=Open+Sans:ital,wght@0,400;0,600;0,700;1,400&display=swap" rel="stylesheet">
<style>
:root{
  --red:#ec1f27;
  --red-dark:#c4161d;
  --ink:#222222;
  --text:#555555;
  --muted:#8a8a8a;
  --line:#e3e3e3;
  --white:#ffffff;
  --panel:#2b2b2b;
  --panel-2:#333333;
  --footer:#262626;
  --footer-bottom:#1c1c1c;
}
*{box-sizing:border-box;margin:0;padding:0}
html,body{width:1200px;height:3096px;overflow:hidden;background:var(--white)}
body{font-family:"Open Sans",Arial,sans-serif;color:var(--text);font-size:13px;line-height:1.6}
.wrap{width:1000px;margin:0 auto;position:relative}
.serif{font-family:"Noto Serif",Georgia,serif}
ul{list-style:none}

/* top bar */
.topbar{height:40px;border-bottom:1px solid var(--line)}
.topbar .wrap{height:40px;display:flex;justify-content:flex-end;align-items:center;font-size:12px;color:var(--muted);gap:8px}
.topbar svg{width:14px;height:14px}

/* header */
.header{height:80px;border-bottom:1px solid var(--line)}
.header .wrap{height:80px;display:flex;justify-content:space-between;align-items:center}
.brand-name{font-weight:700;font-size:34px;color:var(--red);letter-spacing:-0.5px;line-height:1}
.brand-tag{font-size:10px;letter-spacing:2px;color:var(--muted);margin-top:4px}
.nav{display:flex;gap:0;height:80px}
.nav a{display:flex;align-items:center;padding:0 20px;font-size:13px;color:var(--ink);text-decoration:none;border-top:3px solid transparent}
.nav a.active{border-top-color:var(--red);color:var(--red)}

/* hero */
.hero{height:592px;position:relative;background:linear-gradient(110deg,#6b6f73 0%,#9a9c9e 30%,#c9c9c7 55%,#e6e4e0 75%,#b9b6b1 100%);overflow:hidden}
.hero-photo{position:absolute;inset:0}
.hero-copy{position:absolute;left:100px;top:250px}
.hero-title{display:inline-block;background:rgba(236,31,39,.85);color:var(--white);font-size:44px;font-weight:400;letter-spacing:1px;padding:4px 14px;line-height:1.2}
.hero-sub{display:block;width:430px;background:rgba(236,31,39,.85);color:var(--white);font-size:18px;font-weight:600;line-height:1.35;padding:8px 14px;margin-top:6px}
.hero-btn{display:inline-block;background:var(--red-dark);color:var(--white);font-size:11px;padding:6px 12px;margin-top:8px;text-transform:uppercase}
.hero-arrow{position:absolute;top:266px;width:36px;height:60px;background:rgba(40,40,40,.75);display:flex;align-items:center;justify-content:center}
.hero-arrow.left{left:0}.hero-arrow.right{right:0}

/* welcome */
.welcome{height:400px;text-align:center;padding-top:72px}
.welcome h1{font-family:"Noto Serif",Georgia,serif;font-weight:400;font-size:30px;color:var(--ink)}
.welcome .tagline{font-size:12px;color:var(--muted);margin-top:4px}
.welcome .intro{width:980px;margin:36px auto 0;font-size:12px;color:var(--muted);line-height:1.75}
.consult{margin-top:40px;display:flex;justify-content:center;align-items:center;gap:14px;font-size:14px;color:var(--ink)}
.consult .pill{background:var(--red);color:var(--white);font-weight:700;font-size:17px;padding:6px 18px;border-radius:20px}

/* features band */
.features{height:320px;background:linear-gradient(180deg,#3a3a3a 0%,#262626 100%)}
.features .wrap{display:flex;gap:40px;padding-top:38px}
.feature{flex:1}
.feature-head{display:flex;align-items:center;gap:14px}
.feature-icon{width:48px;height:48px;border:2px solid var(--red);display:flex;align-items:center;justify-content:center}
.feature h3{font-family:"Noto Serif",Georgia,serif;font-weight:400;font-size:24px;color:var(--white)}
.feature p{color:#a8a8a8;font-size:12px;margin:18px 0 0 62px;line-height:1.7}
.feature .btn{display:inline-block;margin:24px 0 0 62px;border:1px solid #777;border-bottom:2px solid var(--red);color:var(--white);font-size:12px;padding:8px 22px}

/* three columns */
.info{height:548px;padding-top:60px}
.info .wrap{display:flex;gap:44px}
.info .col{flex:1}
.info h2{font-family:"Noto Serif",Georgia,serif;font-weight:400;font-size:32px;color:var(--ink);margin-bottom:22px}
.acc-item{height:44px;display:flex;align-items:center;justify-content:space-between;padding:0 16px;background:var(--panel);color:var(--white);font-size:13px;margin-bottom:4px}
.acc-item.open{background:var(--red)}
.acc-body{display:flex;gap:14px;padding:16px 0 18px}
.acc-thumb{width:74px;height:74px;background:linear-gradient(135deg,#5b5b5b,#2e2e2e)}
.acc-body p{font-size:12px;color:var(--muted);flex:1}
.services p{font-size:12px;color:var(--muted);line-height:1.75}
.services li{display:flex;align-items:center;gap:10px;height:38px;border-bottom:1px solid var(--line);font-size:12px;color:var(--text)}
.services li svg{width:10px;height:10px}
.services ul{margin-top:14px}
.tabs{display:flex;gap:6px;border-bottom:2px solid var(--red)}
.tab{padding:8px 16px;font-size:12px;color:var(--text);background:#f2f2f2}
.tab.active{background:var(--red);color:var(--white)}
.adv-img{height:190px;margin-top:14px;background:linear-gradient(135deg,#d8c9a6 0%,#8a6f48 50%,#3b2d1d 100%)}
.adv-text{font-size:12px;color:var(--muted);margin-top:14px;line-height:1.7}

/* photo strip */
.strip{height:260px;display:flex}
.strip .tile{flex:1;position:relative}
.t1{background:linear-gradient(135deg,#6b6b6b,#2f2f2f)}
.t2{background:linear-gradient(135deg,#e2535a,#a8161c)}
.t3{background:linear-gradient(135deg,#caa273,#5f3f22)}
.t4{background:linear-gradient(135deg,#c7ccd3,#5a6674)}
.t5{background:linear-gradient(135deg,#ececec,#9a9a9a)}
.strip .zoom{position:absolute;left:50%;top:50%;width:56px;height:56px;margin:-28px 0 0 -28px;border:2px solid var(--white);border-radius:50%;display:flex;align-items:center;justify-content:center}

/* passion */
.passion{height:360px;text-align:center;padding-top:66px}
.passion h2{font-family:"Noto Serif",Georgia,serif;font-weight:400;font-size:40px;line-height:1.25;color:var(--ink)}
.passion h2 em{font-style:normal;color:var(--red)}
.quote{width:620px;margin:30px auto 0;position:relative;font-style:italic;font-size:13px;color:var(--muted);line-height:1.7}
.quote .mark{position:absolute;top:-8px;color:var(--red);font-size:34px;font-family:"Noto Serif",Georgia,serif;font-style:normal}
.quote .mark.l{left:-46px}.quote .mark.r{right:-46px}
.author{margin-top:22px;font-size:11px;color:var(--muted)}

/* footer */
.footer{height:416px;background:var(--footer);padding-top:40px}
.footer .wrap{display:flex;gap:40px}
.footer .col{flex:1}
.footer h4{font-family:"Noto Serif",Georgia,serif;font-weight:400;font-size:20px;color:var(--white);padding-bottom:12px;border-bottom:1px solid #3d3d3d;margin-bottom:16px}
.footer p,.footer li{font-size:11px;color:#9a9a9a;line-height:1.8}
.contact-lines p{margin-bottom:8px}
.links li{display:flex;align-items:center;gap:8px;height:27px;border-bottom:1px solid #333}
.links li svg{width:8px;height:8px}
.tweet{margin-bottom:16px}
.tweet .handle{color:var(--red)}
.tweet .time{display:block;color:#6d6d6d;font-size:10px}
.field{height:32px;background:#1d1d1d;border:1px solid #3a3a3a;margin-bottom:8px;font-size:11px;color:#777;padding:7px 10px}
.field.area{height:84px}
.submit{display:inline-block;background:var(--red);color:var(--white);font-size:11px;padding:7px 16px}
.copyright{height:36px;background:var(--footer-bottom)}
.copyright .wrap{height:36px;display:flex;align-items:center;font-size:11px;color:#777}
</style>
</head>
<body>

<div class="topbar">
  <div class="wrap">
    <svg viewBox="0 0 24 24" fill="#ec1f27"><path d="M6.6 10.8a15.2 15.2 0 0 0 6.6 6.6l2.2-2.2c.3-.3.7-.4 1-.2 1.1.4 2.3.6 3.6.6.6 0 1 .4 1 1V20c0 .6-.4 1-1 1A17 17 0 0 1 3 4c0-.6.4-1 1-1h3.5c.6 0 1 .4 1 1 0 1.3.2 2.5.6 3.6.1.3 0 .7-.2 1z"/></svg>
    <span>Call Us: (866) 123-456-7890</span>
  </div>
</div>

<header class="header">
  <div class="wrap">
    <div class="brand">
      <div class="brand-name">FenderPals</div>
      <div class="brand-tag">PERSONAL INJURY LAWYERS</div>
    </div>
    <nav class="nav">
      <a class="active">Home</a>
      <a>Client Resources</a>
      <a>Expertise / Car Wrecks</a>
      <a>News</a>
      <a>Contact Us</a>
    </nav>
  </div>
</header>

<section class="hero">
  <div class="hero-photo" role="img" aria-label="Photo of a distressed driver holding his head beside a damaged car after a wreck"></div>
  <div class="hero-copy">
    <div class="hero-title">GET LEGAL HELP FROM US</div>
    <div class="hero-sub">Lorem Ipsum is simply dummy text of the printing and typesetting industry. Lorem Ipsum dummy text.</div>
    <div class="hero-btn">Learn more</div>
  </div>
  <div class="hero-arrow left"><svg width="12" height="20" viewBox="0 0 12 20"><path d="M10 2 2 10l8 8" fill="none" stroke="#fff" stroke-width="2.5"/></svg></div>
  <div class="hero-arrow right"><svg width="12" height="20" viewBox="0 0 12 20"><path d="m2 2 8 8-8 8" fill="none" stroke="#fff" stroke-width="2.5"/></svg></div>
</section>

<section class="welcome">
  <h1>Welcome to Law Firm - Providing Legal Help</h1>
  <div class="tagline">Experience. Reliability. Ethics.</div>
  <p class="intro">Every car wreck leaves more than bent metal behind. Our team handles one kind of case only, so every hour we spend is spent on drivers and passengers who were hurt on the road. We listen first, gather the facts of the crash, deal with the insurers, and keep you informed at each step while you focus on getting better. If you are injured in a collision, call us for a free review of your case; there is no fee unless we recover compensation for you. Our lawyers are available day and night to answer your questions.</p>
  <div class="consult">
    <span>Get your Free Consultation</span>
    <span class="pill">(866) 123-456-7890</span>
    <span>Available 24/7</span>
  </div>
</section>

<section class="features">
  <div class="wrap">
    <div class="feature">
      <div class="feature-head">
        <div class="feature-icon"><svg width="22" height="22" viewBox="0 0 24 24" fill="none" stroke="#fff" stroke-width="2"><path d="M6 2h9l4 4v16H6z"/><path d="M9 11h7M9 15h7"/></svg></div>
        <h3>Request Quote</h3>
      </div>
      <p>Consectetur sadipscing elitr, sed diam nonumy eirmod tempor invidunt ut labore et dolore magna.</p>
      <div class="btn">Send Request</div>
    </div>
    <div class="feature">
      <div class="feature-head">
        <div class="feature-icon"><svg width="22" height="22" viewBox="0 0 24 24" fill="none" stroke="#fff" stroke-width="2"><circle cx="10" cy="10" r="6"/><path d="m15 15 6 6"/></svg></div>
        <h3>Case Investigation</h3>
      </div>
      <p>Consectetur sadipscing elitr, sed diam nonumy eirmod tempor invidunt ut labore et dolore magna.</p>
      <div class="btn">Know More</div>
    </div>
    <div class="feature">
      <div class="feature-head">
        <div class="feature-icon"><svg width="22" height="22" viewBox="0 0 24 24" fill="none" stroke="#fff" stroke-width="2"><path d="M12 3 4 6v6c0 5 3.5 8 8 9 4.5-1 8-4 8-9V6z"/></svg></div>
        <h3>Case Fight</h3>
      </div>
      <p>Consectetur sadipscing elitr, sed diam nonumy eirmod tempor invidunt ut labore et dolore magna.</p>
      <div class="btn">View Details</div>
    </div>
  </div>
</section>

<section class="info">
  <div class="wrap">
    <div class="col why">
      <h2>Why Us?</h2>
      <div class="acc-item open"><span>Consectetur sadipscing</span><svg width="10" height="10" viewBox="0 0 10 10"><path d="m1 3 4 4 4-4" fill="none" stroke="#fff" stroke-width="1.8"/></svg></div>
      <div class="acc-body">
        <div class="acc-thumb" role="img" aria-label="Small photo of a lawyer with a client"></div>
        <p>Labore dolore magna aliquyam erat sed diam voluptua at vero eos et accusam.</p>
      </div>
      <div class="acc-item"><span>Eirmod diam nonumy</span><svg width="10" height="10" viewBox="0 0 10 10"><path d="m3 1 4 4-4 4" fill="none" stroke="#fff" stroke-width="1.8"/></svg></div>
      <div class="acc-item"><span>Tempor invidunt</span><svg width="10" height="10" viewBox="0 0 10 10"><path d="m3 1 4 4-4 4" fill="none" stroke="#fff" stroke-width="1.8"/></svg></div>
      <div class="acc-item"><span>Ut labore et dolore magna</span><svg width="10" height="10" viewBox="0 0 10 10"><path d="m3 1 4 4-4 4" fill="none" stroke="#fff" stroke-width="1.8"/></svg></div>
      <div class="acc-item"><span>Usquam erat, sed diam</span><svg width="10" height="10" viewBox="0 0 10 10"><path d="m3 1 4 4-4 4" fill="none" stroke="#fff" stroke-width="1.8"/></svg></div>
    </div>

    <div class="col services">
      <h2>Services</h2>
      <p>Lorem ipsum dolor sit amet, consetetur sadipscing elitr, sed diam nonumy eirmod tempor invidunt ut labore et dolore magna aliquyam erat, sed diam voluptua at vero eos et accusam.</p>
      <ul>
        <li><svg viewBox="0 0 10 10"><path d="m2 1 5 4-5 4" fill="none" stroke="#ec1f27" stroke-width="2"/></svg>At vero eos et accusam</li>
        <li><svg viewBox="0 0 10 10"><path d="m2 1 5 4-5 4" fill="none" stroke="#ec1f27" stroke-width="2"/></svg>Stet clita kasd gubergren no sea</li>
        <li><svg viewBox="0 0 10 10"><path d="m2 1 5 4-5 4" fill="none" stroke="#ec1f27" stroke-width="2"/></svg>Takimata sanctus est</li>
        <li><svg viewBox="0 0 10 10"><path d="m2 1 5 4-5 4" fill="none" stroke="#ec1f27" stroke-width="2"/></svg>Lorem ipsum dolor sit amet</li>
        <li><svg viewBox="0 0 10 10"><path d="m2 1 5 4-5 4" fill="none" stroke="#ec1f27" stroke-width="2"/></svg>Consetetur sadipscing</li>
      </ul>
    </div>

    <div class="col advantages">
      <h2>Advantages</h2>
      <div class="tabs">
        <div class="tab active">Quality</div>
        <div class="tab">Services</div>
        <div class="tab">Results</div>
      </div>
      <div class="adv-img" role="img" aria-label="Close-up photo on a wooden desk in warm brown tones"></div>
      <p class="adv-text">Consetetur sadipscing elitr, sed diam nonumy eirmod tempor invidunt ut labore et dolore magna aliquyam erat, sed diam voluptua.</p>
    </div>
  </div>
</section>

<section class="strip">
  <div class="tile t1" role="img" aria-label="Photo of paperwork on a desk"></div>
  <div class="tile t2" role="img" aria-label="Photo with red highlight overlay of a consultation">
    <div class="zoom"><svg width="24" height="24" viewBox="0 0 24 24" fill="none" stroke="#fff" stroke-width="2.2"><circle cx="10" cy="10" r="6"/><path d="m15 15 6 6"/></svg></div>
  </div>
  <div class="tile t3" role="img" aria-label="Photo of a meeting at a wooden table"></div>
  <div class="tile t4" role="img" aria-label="Photo of a lawyer in a suit"></div>
  <div class="tile t5" role="img" aria-label="Photo of a hand signing a document"></div>
</section>

<section class="passion">
  <h2>We are <em>Passionate About Helping</em> Clients Achieve<br>Their Goals</h2>
  <div class="quote">
    <span class="mark l">&ldquo;</span>
    At vero eos et accusam et justo duo dolores et ea rebum, stet clita kasd gubergren, no sea takimata sanctus est lorem ipsum dolor sit amet, lorem ipsum dolor sit amet consetetur.
    <span class="mark r">&rdquo;</span>
  </div>
  <div class="author">- admin -</div>
</section>

<footer class="footer">
  <div class="wrap">
    <div class="col contact-lines">
      <h4>Contact</h4>
      <p>FenderPals Personal Injury Lawyers</p>
      <p>Head Office<br>Harbor Point, 48 Linden Avenue<br>Suite 200</p>
      <p>Phone: (866) 123-456-7890<br>Fax: (866) 123-456-7891</p>
      <p>Open: Mon–Fri 9am–5pm<br>Emergency: 24/7</p>
      <p>hello@fenderpals-example.com</p>
    </div>
    <div class="col links">
      <h4>Quick Links</h4>
      <ul>
        <li><svg viewBox="0 0 10 10"><path d="m2 1 5 4-5 4" fill="none" stroke="#ec1f27" stroke-width="2"/></svg>Consectetur adipiscing</li>
        <li><svg viewBox="0 0 10 10"><path d="m2 1 5 4-5 4" fill="none" stroke="#ec1f27" stroke-width="2"/></svg>Nonumy eirmod tempor</li>
        <li><svg viewBox="0 0 10 10"><path d="m2 1 5 4-5 4" fill="none" stroke="#ec1f27" stroke-width="2"/></svg>Invidunt ut labore</li>
        <li><svg viewBox="0 0 10 10"><path d="m2 1 5 4-5 4" fill="none" stroke="#ec1f27" stroke-width="2"/></svg>Dolore magna aliquyam</li>
        <li><svg viewBox="0 0 10 10"><path d="m2 1 5 4-5 4" fill="none" stroke="#ec1f27" stroke-width="2"/></svg>Sed diam voluptua</li>
        <li><svg viewBox="0 0 10 10"><path d="m2 1 5 4-5 4" fill="none" stroke="#ec1f27" stroke-width="2"/></svg>Vero eos et accusam</li>
        <li><svg viewBox="0 0 10 10"><path d="m2 1 5 4-5 4" fill="none" stroke="#ec1f27" stroke-width="2"/></svg>Justo duo dolores</li>
      </ul>
    </div>
    <div class="col tweets">
      <h4>Latest Tweets</h4>
      <p class="tweet"><span class="handle">@fenderpals</span> Lorem ipsum dolor sit amet, consetetur sadipscing elitr sed diam nonumy. <span class="time">2 days ago</span></p>
      <p class="tweet"><span class="handle">@fenderpals</span> Eirmod tempor invidunt ut labore et dolore magna aliquyam erat sed. <span class="time">4 days ago</span></p>
      <p class="tweet"><span class="handle">@fenderpals</span> At vero eos et accusam et justo duo dolores et ea rebum stet. <span class="time">1 week ago</span></p>
    </div>
    <div class="col form">
      <h4>Contact Us</h4>
      <div class="field">Full Name</div>
      <div class="field">Email Address</div>
      <div class="field">Subject</div>
      <div class="field area">Message</div>
      <div class="submit">Submit</div>
    </div>
  </div>
</footer>

<div class="copyright">
  <div class="wrap">Copyright &copy; 2015 FenderPals. All Rights Reserved.</div>
</div>

</body>
</html>
```